Dental office Stationary & Business card
Marlowe Pines Dental LLC
Dental office Stationary & Business card - Health
Creative Brief
Professional
Implants- Cosmetics- Generals- Braces
2815 Quarry Hollow Pkwy. Unit 3407 Norcross, GA 30071
mpdoffice@tinmail.example
www.marlowepinesdental.example
We would like designers to include for us the following: business card, letter head, envelope label, and e-signature template. logo design files can be downloaded below: https://www.filecrate.example/s/q8zrt3mw1xk5pa/Modern%20logo%20for%20a%20dental%20office.zip
Please have this content in the back of the card. "Your next appointment is on ____________ at _______ AM/PM

```html
<!DOCTYPE html>
<html lang="en">
<head>
<meta charset="utf-8">
<title>Marlowe Pines Dental – Business Card</title>
<link rel="stylesheet" href="https://fonts.googleapis.com/css2?family=Montserrat:wght@400;500;600&display=swap">
<style>
  :root {
    --stage: #3b3b3d;
    --card: #ffffff;
    --brown: #6b3a22;
    --brown-deep: #4a2312;
    --brown-light: #87502f;
    --cream: #f3e7dc;
  }
  * { margin: 0; padding: 0; box-sizing: border-box; }
  html, body { width: 1200px; height: 770px; overflow: hidden; }
  body {
    background: var(--stage);
    font-family: "Montserrat", sans-serif;
    position: relative;
  }
  .card {
    position: absolute;
    width: 540px;
    height: 310px;
    background: var(--card);
    border-radius: 14px;
    overflow: hidden;
    box-shadow: 0 10px 30px rgba(0,0,0,.35);
  }
  .card--front { left: 50px; top: 70px; }
  .card--back { left: 610px; top: 390px; }

  .brand {
    display: flex;
    align-items: center;
    gap: 12px;
    color: var(--brown);
    font-weight: 600;
    text-transform: uppercase;
    letter-spacing: 2px;
  }
  .brand__dot {
    width: 18px; height: 18px;
    border-radius: 50%;
    background: var(--brown);
    flex: none;
  }
  .card--front .brand {
    position: absolute;
    left: 0; right: 0; top: 112px;
    justify-content: center;
    font-size: 22px;
  }
  .appointment {
    position: absolute;
    left: 0; right: 0; top: 190px;
    text-align: center;
    color: var(--brown);
    font-size: 11px;
    font-weight: 500;
    letter-spacing: .5px;
  }
  .card--back .brand {
    position: absolute;
    left: 150px; top: 48px;
    font-size: 18px;
  }

  .band { position: absolute; left: 0; top: 0; width: 540px; height: 310px; }

  .contact-person {
    position: absolute;
    left: 150px; top: 175px;
    color: var(--cream);
    text-align: right;
    width: 150px;
  }
  .contact-person__name { font-size: 12px; font-weight: 500; letter-spacing: 1.5px; text-transform: uppercase; }
  .contact-person__role { font-size: 8px; margin-top: 3px; letter-spacing: 1px; }
  .contact-address {
    position: absolute;
    left: 150px; top: 218px;
    width: 150px;
    text-align: right;
    color: var(--cream);
    font-size: 8px;
    line-height: 1.5;
    letter-spacing: .5px;
  }
  .divider {
    position: absolute;
    left: 318px; top: 175px;
    width: 1px; height: 80px;
    background: rgba(243,231,220,.45);
  }
  .contact-list {
    position: absolute;
    left: 334px; top: 170px;
    list-style: none;
    color: var(--cream);
    font-size: 8.5px;
    letter-spacing: .4px;
  }
  .contact-list li {
    display: flex; align-items: center; gap: 7px;
    height: 18px;
  }
  .contact-list svg { width: 11px; height: 11px; flex: none; }
</style>
</head>
<body>

  <section class="card card--front" aria-label="Business card front">
    <div class="brand"><span class="brand__dot"></span>Marlowe Pines Dental</div>
    <p class="appointment">Your next appointment is on ____________ at _______ AM/PM</p>
  </section>

  <section class="card card--back" aria-label="Business card back">
    <svg class="band" viewBox="0 0 540 310" aria-hidden="true">
      <defs>
        <linearGradient id="bandFill" x1="0" y1="0" x2="0" y2="1">
          <stop offset="0" stop-color="#87502f"/>
          <stop offset="1" stop-color="#4a2312"/>
        </linearGradient>
      </defs>
      <path d="M0 148 C150 128 330 128 540 112 L540 310 L0 310 Z" fill="#c9a58c" opacity=".5"/>
      <path d="M0 158 C160 138 340 140 540 124 L540 310 L0 310 Z" fill="url(#bandFill)"/>
      <path d="M0 164 C160 146 340 148 540 132" fill="none" stroke="#f3e7dc" stroke-width="1.5" opacity=".8"/>
    </svg>

    <div class="brand"><span class="brand__dot"></span>Marlowe Pines Dental</div>

    <div class="contact-person">
      <p class="contact-person__name">Reid Calloway</p>
      <p class="contact-person__role">Owner / C.E.O</p>
    </div>
    <p class="contact-address">2815 Quarry Hollow Pkwy.<br>Unit 3407<br>Norcross, GA 30071</p>
    <span class="divider"></span>

    <ul class="contact-list">
      <li><svg viewBox="0 0 12 12"><circle cx="6" cy="6" r="6" fill="#f3e7dc"/><path d="M4 3.2l1 1.3-.6.8c.4.9 1.1 1.6 2 2l.8-.6 1.3 1-.6 1.1C5.8 8.6 3.4 6.2 3.2 3.8z" fill="#6b3a22"/></svg>555-014-2280</li>
      <li><svg viewBox="0 0 12 12"><circle cx="6" cy="6" r="6" fill="#f3e7dc"/><rect x="4.2" y="2.8" width="3.6" height="6.4" rx=".6" fill="#6b3a22"/></svg>555-019-4471</li>
      <li><svg viewBox="0 0 12 12"><circle cx="6" cy="6" r="6" fill="#f3e7dc"/><rect x="3" y="4" width="6" height="4.4" fill="#6b3a22"/></svg>555-012-6603</li>
      <li><svg viewBox="0 0 12 12"><circle cx="6" cy="6" r="6" fill="#f3e7dc"/><rect x="3" y="4" width="6" height="4" fill="none" stroke="#6b3a22" stroke-width=".9"/><path d="M3 4l3 2.2L9 4" fill="none" stroke="#6b3a22" stroke-width=".9"/></svg>mpdoffice@tinmail.example</li>
      <li><svg viewBox="0 0 12 12"><circle cx="6" cy="6" r="6" fill="#f3e7dc"/><circle cx="6" cy="6" r="3" fill="none" stroke="#6b3a22" stroke-width=".9"/><path d="M3 6h6M6 3v6" stroke="#6b3a22" stroke-width=".7"/></svg>www.marlowepinesdental.example</li>
    </ul>
  </section>

</body>
</html>
```